Micro-Marketing and Vending Brochure

I am looking for an elegant, fun, eye catching brochure that will highlight my new business to protential clients in the Hotel, College/University and Hospital industry. please find pictures of Micro-Markets on line and on my website, to make a fun, professional and elegant design, use color scheme from website, and logo and a few picture will be attach to this email. This is a new business and i would like to represent my company in the best possible way, please take time with this project, color, front and wording is very important along with pics. I have a image of a micro-Market please take out the BRISKO and place file logo of TORN..please let me know if more information is needed for this project to be successful

```html
<!DOCTYPE html>
<html lang="en">
<head>
<meta charset="utf-8">
<title>Velmora Micro-Market Brochure</title>
<link href="https://fonts.googleapis.com/css2?family=Raleway:wght@400;500;600;700&family=Oswald:wght@600&display=swap" rel="stylesheet">
<style>
  :root{
    --navy:#2c3355;
    --purple:#7760ad;
    --purple-deep:#4e3d7a;
    --gold:#e6bc47;
    --gold-text:#c9a23c;
    --paper:#f1f2f7;
    --ink:#3a3d52;
    --stage:#5f6b5e;
  }
  *{margin:0;padding:0;box-sizing:border-box}
  html,body{width:1200px;height:914px;overflow:hidden}
  body{background:var(--stage);font-family:"Raleway",sans-serif;color:var(--ink);position:relative}
  .spread{position:absolute;left:40px;top:62px;width:1120px;height:790px;display:flex;box-shadow:0 12px 30px rgba(0,0,0,.35)}
  .page{position:relative;width:560px;height:790px;overflow:hidden;background:var(--paper)}
  .page svg.bg{position:absolute;inset:0}
  .brand{position:absolute;display:flex;align-items:center;gap:10px;font-family:"Raleway",sans-serif;font-weight:700;letter-spacing:3px}
  .brand .mark{width:22px;height:22px;background:var(--gold)}
  /* back cover */
  .back-title{position:absolute;left:48px;top:122px;font-size:24px;font-weight:700;line-height:1.2;color:var(--navy)}
  .back-title span{display:block;color:var(--gold-text)}
  .back-title::after{content:"";display:block;width:70px;height:2px;background:var(--purple);margin-top:8px}
  .back-body{position:absolute;left:48px;top:205px;width:464px;font-size:13px;line-height:1.5;color:var(--ink)}
  .back-body p+p{margin-top:6px}
  .quote{position:absolute;left:40px;top:365px;width:480px;text-align:center;font-size:21px;line-height:1.35;color:var(--ink)}
  .quote em{font-style:normal;color:var(--gold-text);font-weight:600}
  .quote cite{display:block;font-style:normal;font-size:16px;margin-top:4px}
  .portrait{position:absolute;left:362px;top:490px;width:140px;height:140px;border-radius:50%;border:7px solid var(--navy);box-shadow:0 0 0 6px var(--gold);background:radial-gradient(circle at 50% 40%,#f4f1ee,#d9c9c4 55%,#b6556a)}
  .contact{position:absolute;left:48px;top:652px;font-size:14px;line-height:1.5;color:var(--navy)}
  .contact h3{font-size:16px;font-weight:700;margin-bottom:4px}
  .contact h3 span{color:var(--gold-text)}
  .contact li{list-style:none;display:flex;align-items:center;gap:8px}
  .contact svg{width:12px;height:12px;flex:none}
  .back-brand{right:40px;top:690px;font-size:24px;color:var(--navy)}
  /* front cover */
  .photo{position:absolute;left:0;top:0;width:560px;height:600px;background:linear-gradient(180deg,#cfd9ea 0%,#e9eef5 30%,#a9b88a 62%,#6f8a48 100%)}
  .front-brand{left:40px;top:40px;font-size:30px;color:#fff}
  .headline{position:absolute;left:56px;top:330px;font-family:"Oswald",sans-serif;font-weight:600;font-size:50px;line-height:1.02;color:#fff;text-transform:uppercase;text-shadow:2px 2px 4px rgba(0,0,0,.45)}
  .front-title{position:absolute;right:40px;top:598px;text-align:right;font-size:26px;font-weight:600;line-height:1.3;color:var(--navy)}
  .front-title span{display:block;color:var(--gold-text)}
  .call{position:absolute;right:40px;top:690px;background:var(--purple-deep);color:#fff;font-weight:700;font-size:17px;padding:12px 26px;border-radius:22px 22px 0 0}
</style>
</head>
<body>
<div class="spread">
  <section class="page page--back">
    <svg class="bg" viewBox="0 0 560 790" width="560" height="790" aria-hidden="true">
      <path d="M0 0H560V110C470 70 380 60 280 80C180 100 90 110 0 92Z" fill="var(--navy)"/>
      <path d="M0 100C90 118 180 108 280 88C380 68 470 78 560 118" fill="none" stroke="var(--gold)" stroke-width="4"/>
      <path d="M0 565C140 540 300 585 560 560V790H0Z" fill="var(--gold)"/>
      <path d="M0 578C140 554 300 598 560 574V790H0Z" fill="var(--purple)"/>
      <path d="M0 605C120 596 260 622 560 600V790H0Z" fill="var(--navy)"/>
      <path d="M0 660C100 632 300 622 560 622V790H0Z" fill="var(--paper)"/>
    </svg>
    <h2 class="back-title">Micro-Market &amp;<span>Healthy Vending Solution</span></h2>
    <div class="back-body">
      <p>Offering a large variety of healthy, nutritious products in an affordable and efficient manner. There is an increasing demand for products that suit a more healthier lifestyle, we understand those needs and strive for a wide selection of healthier types of products.</p>
      <p>Offering Special design solutions for Micro-Markets in Break-rooms, Office Buildings, Hotels and colleges hangout areas.</p>
    </div>
    <blockquote class="quote">A business has to be involving, it has to be fun, and it has to exercise <em>your creative instincts..</em><cite>— Daniel Ashcombe</cite></blockquote>
    <div class="portrait" role="img" aria-label="Photo of a smiling girl holding out a glass of red juice"></div>
    <div class="contact">
      <h3><span>Contact</span> Today :</h3>
      <ul>
        <li><svg viewBox="0 0 12 12"><path d="M6 1a3.5 3.5 0 0 0-3.5 3.5C2.5 7 6 11 6 11s3.5-4 3.5-6.5A3.5 3.5 0 0 0 6 1z" fill="none" stroke="var(--gold)" stroke-width="1.3"/></svg>VELMORA MARKETS LLC, 10482, USA</li>
        <li><svg viewBox="0 0 12 12"><path d="M3 1l2 2.5-1.2 1.2a6 6 0 0 0 3.5 3.5L8.5 7 11 9l-1.5 2C5 11 1 7 1 2.5z" fill="none" stroke="var(--gold)" stroke-width="1.2"/></svg>1-800-555-0147</li>
        <li><svg viewBox="0 0 12 12"><rect x="1" y="2.5" width="10" height="7" fill="none" stroke="var(--gold)" stroke-width="1.2"/><path d="M1 2.5l5 4 5-4" fill="none" stroke="var(--gold)" stroke-width="1.2"/></svg>INFO@VELMORAMARKETS.COM</li>
        <li><svg viewBox="0 0 12 12"><circle cx="6" cy="6" r="5" fill="var(--gold)"/></svg>www.velmoramarkets.com</li>
      </ul>
    </div>
    <div class="brand back-brand"><span class="mark"></span>VELMORA</div>
  </section>

  <section class="page page--front">
    <div class="photo" role="img" aria-label="Photo of a happy family with children running across a sunny park lawn"></div>
    <svg class="bg" viewBox="0 0 560 790" width="560" height="790" aria-hidden="true">
      <path d="M0 0H560V40C440 60 360 150 230 150C140 150 60 130 0 140Z" fill="var(--navy)"/>
      <path d="M0 148C60 138 140 158 230 158C360 158 440 68 560 48" fill="none" stroke="var(--gold)" stroke-width="4"/>
      <path d="M0 520C200 530 380 480 560 395V790H0Z" fill="var(--gold)"/>
      <path d="M0 540C200 548 380 500 560 420V790H0Z" fill="var(--purple)"/>
      <path d="M0 568C220 580 400 540 560 480V790H0Z" fill="var(--navy)"/>
      <path d="M0 585C220 600 400 570 560 515V790H0Z" fill="var(--paper)"/>
    </svg>
    <div class="brand front-brand"><span class="mark"></span>VELMORA</div>
    <h1 class="headline">Healthy<br>Happy Snack<br>People</h1>
    <h2 class="front-title">Micro-Market &amp;<span>Healthy Vending Solution</span></h2>
    <div class="call">Call Today : 1-800-555-0147</div>
  </section>
</div>
</body>
</html>
```